Salt Water Delivery Company Business Card Design

We are a company that delivers natural saltwater (from the ocean) to aquarium companies, restaurants and home marine tanks. I would like a new business card to suit.

Must include Name, company name, abn, contact number and website as well as logo (see attached).

Looking for a design that stands out, has a clean but unique appearance.

Double and single sided entries welcome

Industry/Entity Type

Business

Requirements
Must have
• Logo

```html
<!DOCTYPE html>
<html lang="en">
<head>
<meta charset="utf-8">
<title>Tidal Haul Business Card</title>
<link rel="stylesheet" href="https://fonts.googleapis.com/css2?family=Ubuntu:wght@400;500;700&display=swap">
<style>
  :root {
    --page-bg: #e9ecef;
    --card-top: #b9dcf3;
    --card-mid: #dcedf8;
    --card-bottom: #ffffff;
    --brand-blue: #1d83c6;
    --deep-blue: #1a5f9e;
    --ink-blue: #1b4f86;
    --text-grey: #2f3a44;
    --water-light: #9fd0f0;
    --water-deep: #2a6fb6;
  }
  * { margin: 0; padding: 0; box-sizing: border-box; }
  html, body { width: 1200px; height: 861px; overflow: hidden; }
  body {
    background: var(--page-bg);
    font-family: "Ubuntu", sans-serif;
    display: flex;
    align-items: center;
    justify-content: center;
    gap: 60px;
  }
  .card {
    position: relative;
    width: 520px;
    height: 316px;
    border-radius: 14px;
    overflow: hidden;
    box-shadow: 0 10px 30px rgba(0,0,0,0.18);
  }
  .card--front {
    background: linear-gradient(180deg, var(--card-top) 0%, var(--card-mid) 50%, var(--card-bottom) 100%);
  }
  .card--back {
    background: linear-gradient(180deg, var(--card-top) 0%, var(--card-mid) 45%, var(--card-bottom) 75%);
  }
  .brand {
    display: flex;
    align-items: center;
    gap: 12px;
  }
  .brand__dot {
    border-radius: 50%;
    background: var(--brand-blue);
  }
  .brand__name {
    font-weight: 700;
    color: var(--brand-blue);
    letter-spacing: -0.5px;
    line-height: 1;
  }
  .card--front .brand {
    position: absolute;
    left: 70px;
    top: 92px;
  }
  .card--front .brand__dot { width: 34px; height: 34px; }
  .card--front .brand__name { font-size: 60px; }
  .card--front .brand__sub {
    position: absolute;
    left: 118px;
    top: 166px;
    font-size: 21px;
    font-weight: 500;
    color: var(--deep-blue);
  }
  .tagline {
    font-weight: 700;
    color: var(--deep-blue);
  }
  .card--front .tagline {
    position: absolute;
    left: 70px;
    top: 232px;
    font-size: 19px;
  }
  .holder {
    position: absolute;
    left: 28px;
    top: 30px;
    font-size: 28px;
    font-weight: 500;
    color: var(--ink-blue);
  }
  .contact {
    position: absolute;
    left: 30px;
    top: 84px;
    border-collapse: collapse;
    font-size: 12.5px;
  }
  .contact th {
    text-align: left;
    font-weight: 400;
    color: var(--ink-blue);
    padding: 0 14px 3px 0;
  }
  .contact td { color: var(--text-grey); padding-bottom: 3px; }
  .card--back .brand {
    position: absolute;
    right: 30px;
    top: 62px;
    gap: 7px;
  }
  .card--back .brand__dot { width: 14px; height: 14px; }
  .card--back .brand__name { font-size: 27px; }
  .card--back .brand__sub {
    position: absolute;
    right: 46px;
    top: 94px;
    font-size: 10px;
    font-weight: 500;
    color: var(--deep-blue);
  }
  .card--back .tagline {
    position: absolute;
    right: 22px;
    top: 128px;
    font-size: 9.5px;
  }
  .water {
    position: absolute;
    left: 0;
    bottom: 0;
    width: 520px;
    height: 150px;
  }
</style>
</head>
<body>
  <section class="card card--front">
    <div class="brand">
      <span class="brand__dot"></span>
      <span class="brand__name">Tidal Haul</span>
    </div>
    <p class="brand__sub">Seawater Supply</p>
    <p class="tagline">Natural saltwater delivered to your door</p>
  </section>

  <section class="card card--back">
    <h1 class="holder">Reid Morgan</h1>
    <table class="contact">
      <tr><th>Mobile</th><td>0400 123 456</td></tr>
      <tr><th>Website</th><td>www.tidalhaul.com.au</td></tr>
      <tr><th>E-mail</th><td>info@tidalhaul.com.au</td></tr>
      <tr><th>ABN</th><td>12 345 678 901</td></tr>
    </table>
    <div class="brand">
      <span class="brand__dot"></span>
      <span class="brand__name">Tidal Haul</span>
    </div>
    <p class="brand__sub">Seawater Supply</p>
    <p class="tagline">Natural saltwater delivered to your door</p>
    <svg class="water" viewBox="0 0 520 150" role="img" aria-label="Illustration of a blue ocean wave with water bubbles">
      <defs>
        <linearGradient id="waterFill" x1="0" y1="0" x2="0" y2="1">
          <stop offset="0" stop-color="var(--water-light)"/>
          <stop offset="1" stop-color="var(--water-deep)"/>
        </linearGradient>
      </defs>
      <path d="M0 110 C120 95 220 70 330 40 C400 20 470 18 520 20 L520 150 L0 150 Z" fill="url(#waterFill)"/>
    </svg>
  </section>
</body>
</html>
```